Business cards for Wendcycle

We need a business card layout for our new bike and e-bike rental (we also sell used e-bikes and bike accessories). The logo already exists.

```html
<!DOCTYPE html>
<html lang="en">
<head>
<meta charset="utf-8">
<title>Wendcycle business cards</title>
<link rel="stylesheet" href="https://fonts.googleapis.com/css2?family=Montserrat:wght@400;600&family=Fira+Sans:wght@300;500&display=swap">
<style>
  :root {
    --page: #e8e5e0;
    --card-white: #ffffff;
    --card-shade: #ececec;
    --ink: #26343d;
    --teal: #5fbfa3;
    --teal-light: #6dc7ab;
    --slate: #2b3942;
    --white: #ffffff;
  }
  * { margin: 0; padding: 0; box-sizing: border-box; }
  html, body { width: 900px; height: 1200px; overflow: hidden; }
  body {
    position: relative;
    background: var(--page);
    font-family: "Montserrat", Arial, sans-serif;
    color: var(--ink);
  }
  .card {
    position: absolute;
    border-radius: 22px;
    overflow: hidden;
  }
  .card-front {
    left: 87px; top: 126px; width: 733px; height: 428px;
    background: radial-gradient(ellipse at 75% 30%, var(--card-white) 40%, var(--card-shade) 100%);
  }
  .card-back {
    left: 85px; top: 641px; width: 735px; height: 428px;
  }
  .contact {
    position: absolute; left: 53px; top: 124px;
  }
  .contact-name {
    font-weight: 600; font-size: 21px; letter-spacing: 0.5px; line-height: 26px;
  }
  .contact-role {
    font-weight: 600; font-size: 15px; letter-spacing: 0.6px; color: var(--teal); line-height: 20px;
  }
  .contact-address {
    margin-top: 18px; font-size: 15px; line-height: 23px;
  }
  .contact-lines { margin-top: 16px; list-style: none; font-size: 15px; }
  .contact-lines li { display: flex; align-items: center; height: 26px; }
  .contact-lines svg { width: 15px; height: 15px; margin-right: 13px; }
  .brand {
    position: absolute; text-align: center;
  }
  .brand-name {
    font-family: "Fira Sans", Arial, sans-serif;
    font-weight: 300; letter-spacing: 0.5px; line-height: 1; white-space: nowrap;
  }
  .brand-tagline {
    font-family: "Fira Sans", Arial, sans-serif; font-weight: 500; line-height: 1.2;
  }
  .card-front .brand { left: 373px; top: 209px; width: 320px; }
  .card-front .brand-name { font-size: 56px; color: var(--teal); }
  .card-front .brand-tagline { font-size: 20px; margin-top: 22px; color: var(--ink); }
  .back-surface {
    position: absolute; inset: 0;
    background: linear-gradient(60deg, var(--teal-light) 0%, #4f8f84 35%, #3a5356 60%, var(--slate) 100%);
  }
  .card-back .brand { left: 0; width: 100%; top: 194px; }
  .card-back .brand-name { font-size: 64px; color: var(--white); }
  .card-back .brand-tagline { font-size: 18px; margin-top: 30px; color: var(--white); }
</style>
</head>
<body>
  <section class="card card-front">
    <div class="contact">
      <p class="contact-name">MARTIN KELLER</p>
      <p class="contact-role">MANAGING DIRECTOR</p>
      <p class="contact-address">#210 318 Harbour Lane<br>Northfield Canada</p>
      <ul class="contact-lines">
        <li>
          <svg viewBox="0 0 24 24" aria-hidden="true"><path fill="var(--teal)" d="M6.6 10.8a15.1 15.1 0 0 0 6.6 6.6l2.2-2.2c.3-.3.7-.4 1-.2 1.1.4 2.3.6 3.6.6.6 0 1 .4 1 1V20c0 .6-.4 1-1 1A17 17 0 0 1 3 4c0-.6.4-1 1-1h3.5c.6 0 1 .4 1 1 0 1.3.2 2.5.6 3.6.1.3 0 .7-.2 1z"/></svg>
          02 71158302
        </li>
        <li>
          <svg viewBox="0 0 24 24" aria-hidden="true"><rect x="2" y="5" width="20" height="14" fill="var(--teal)"/><path d="M3 6l9 7 9-7" fill="none" stroke="#ffffff" stroke-width="1.6"/></svg>
          martinkeller@wendcycle.com
        </li>
      </ul>
    </div>
    <div class="brand">
      <p class="brand-name">WENDCYCLE</p>
      <p class="brand-tagline">simply ride away</p>
    </div>
  </section>

  <section class="card card-back">
    <div class="back-surface" role="img" aria-label="Faint repeating pattern of brand symbols over a teal-to-slate gradient"></div>
    <div class="brand">
      <p class="brand-name">WENDCYCLE</p>
      <p class="brand-tagline">simply ride away</p>
    </div>
  </section>
</body>
</html>
```